Business card for a boutique travel agency VELARIEN

we need a business card design - double sided. We would like to have a very elegant, sophisticated but modern design. we are travel consultants and our business focus is Europe, mainly the city of Paris. We would like to receive designs in white and silver, black color but if you are confident that we should pick up a color to make it different and more beautful...go ahead! We are going to give business cards to our clients and business partners. It is important to be perceived as elegant, modern and trustful. Please check jpg references.

Target Market(s)

Velarien primary clients are individuals, couples and affinity groups of high-net-worth who travel for leisure at least once per year. Seeking the ultimate travel experience, the target clients demand the finest quality activities and accommodations accompanied by a superior level of service.

Industry/Entity Type

Travel Industry

Contact Information for Business Card

Lucinda Farrow
- lucinda@velarien-example.com
- +55 11 98347.2516
- velarien-example.com
- unique travel experiences (we would like to see this signature printed as a detail)

Font styles to use
Sans Serif

Colors

Designer to choose colors to be used in the design.

Requirements
Must have
• the Velarien logo that I have attached
Nice to have
• we would like to have some nice detail, something different that shows that we care about,... we are detail oriented.
Should not have
• decorative fonts

```html
<!DOCTYPE html>
<html lang="en">
<head>
<meta charset="utf-8">
<title>Velarien — Business Card</title>
<link href="https://fonts.googleapis.com/css2?family=Lato:wght@300;400&display=swap" rel="stylesheet">
<style>
  :root {
    --backdrop: #1d1d1d;
    --card-black: #151515;
    --card-white: #ffffff;
    --ink: #1a1a1a;
    --silver: #9a9a9a;
  }
  html, body {
    margin: 0;
    padding: 0;
    width: 1200px;
    height: 897px;
    overflow: hidden;
    background: var(--backdrop);
    font-family: "Lato", sans-serif;
  }
  .canvas {
    position: relative;
    width: 1200px;
    height: 897px;
  }
  .card {
    position: absolute;
    box-sizing: border-box;
  }
  .card--front {
    left: 353px;
    top: 161px;
    width: 487px;
    height: 278px;
    background: linear-gradient(135deg, #111 0%, #181818 55%, #222 100%);
    display: flex;
    align-items: center;
    justify-content: center;
  }
  .card--front .wordmark {
    color: var(--silver);
    font-size: 33px;
    font-weight: 300;
    letter-spacing: 12px;
    margin-right: -12px;
  }
  .card--back {
    left: 348px;
    top: 468px;
    width: 492px;
    height: 278px;
    background: var(--card-white);
    color: var(--ink);
  }
  .card--back .wordmark {
    position: absolute;
    left: 35px;
    top: 30px;
    font-size: 31px;
    font-weight: 300;
    letter-spacing: 10px;
    line-height: 1;
  }
  .rule {
    position: absolute;
    left: 35px;
    width: 39px;
    height: 1px;
    background: var(--ink);
  }
  .rule--top { top: 97px; }
  .rule--bottom { top: 172px; }
  .holder-name {
    position: absolute;
    left: 35px;
    top: 133px;
    font-size: 15px;
    font-weight: 400;
    letter-spacing: 3px;
    line-height: 1;
    margin: 0;
  }
  .contact {
    position: absolute;
    left: 35px;
    top: 194px;
    margin: 0;
    padding: 0;
    list-style: none;
    font-size: 11.5px;
    letter-spacing: 0.8px;
    line-height: 17.5px;
  }
</style>
</head>
<body>
  <main class="canvas">
    <section class="card card--front" aria-label="Card front">
      <span class="wordmark">VELARIEN</span>
    </section>

    <section class="card card--back" aria-label="Card back">
      <span class="wordmark">VELARIEN</span>
      <div class="rule rule--top"></div>
      <h1 class="holder-name">LUCINDA FARROW</h1>
      <div class="rule rule--bottom"></div>
      <ul class="contact">
        <li>Cell: +55 11 98347.2516</li>
        <li>Email: lucinda@velarien-example.com</li>
        <li>Web: velarien-example.com</li>
      </ul>
    </section>
  </main>
</body>
</html>
```